Marketing / Informational Site for Marriage and Family Therapists Cooperative

We need a web design for a new Marriage and Family Therapist Cooperative, called Meadowgate Counselors. This is a market and information site for potential clients and referrals to learn more about the team and get contact information.

We are looking for profession, clean, and modern design, that cater towards families and mom's concerned about their families mental health and child development.

This should include a home page, an general about page, 3 bio pages (1 for each therapist listed below), and a general contact us page.

Our Domain Name

Meadowgatecounselors.example

Company Name

Meadowgate Counselors

Group Moto/Philosophy

“Our sorrows and wounds are healed only when we touch them with compassion.” - Orvelan

Our Logo

See Heron Final (attached)

Home Page (Introduction)

Feeling stressed and overwhelmed?
Encountering barriers towards your goals?
Having difficulty accomplishing the simplest task?
Have the need to talk but unsure who to turn to?

Therapy can assist you in overcoming all of these challenges. Assist you in uncovering the difficulties and barriers that are keeping you from achieving your life’s ambitions, help discover ways to overcome them, and cope with the impact your behaviour has on your occupation, personal life and social life.

Welcome to our practice, with over 20 years of combined experience in the clinical field you are sure to find the right fit for your needs. Each clinician has experience working with groups, adults, teens, children, families, and couples. We specialize in fostering healthy relationships between individuals, managing depression and anxiety, overcoming trauma, and developing occupational success. Feel free to explore information about each clinician and make an appointment with one of us today.

About Us (bio pics attached)

Marisel Dunkworth

My name is Dr. MariSel Dunkworth and I am a Licensed Marriage Family Therapist with a practice in Riverside, CA. I have devoted my life’s work into developing my skills in this profession. I have over 15 years of experience working in the clinical and the social service settings. These years have afforded me the opportunity to work with groups, families, adults, teens and children with varying symptoms. I have helped clients that have trauma, abuse histories, and many within the legal or social service systems. I enjoy working individuals from all walks of life achieve self sufficiency, social success and occupational success. In my years of training I have come to develop a culturally sensitive practice that centers around the needs of the client.

I have held many positions in my clinical career beginning as clinician moving upwards toward supervisor and program coordinator. I have also over 5 years of experience as an adjunct faculty member in the University setting teaching student to become Marriage and Family Therapists. As a clinician I focused on enriching my clinical skills by developing outcome driven practices to achieve client’s desired goals. As a clinical supervisor, I guided clinicians along their own paths towards clinical licensure. As a program coordinator, I helped develop a clinical assessment and triage program from ground up to assist client in accessing services in the South Los Angeles Area. The program would assist over 100 plus clients on a monthly basis get connected to clinical services and linked to any additional resources as needed by the individual. I have graduated with my, Bachelor’s degree at the Halvern College, Riverside. I received my Masters degree in Clinical Psychology at Mount St. Mary’s University, and my Doctorate degree in Clinical Psychology at Tamsworth Institute.

To schedule an appointment with Dr. MariSel Dunkworth, LMFT:

email: marisel582@postbox.example
Phone: (951)555-0182

Jeb Kowal

My name is Rosalindra (Jeb) Kowal, I received my Masters Degree of Counseling in Marriage and Family Therapy from Corvell Bay State College in June 2000. I have acquired over 15 years of experience helping Individuals, Couples, and Families cope with issues of Anxiety, Depression, Grief and Bereavement, and HIV/AIDS.

I am a Family Systems Therapist and I truly believe the dynamics in our family of origin greatly shape our current belief systems and behaviors. However, I often utilize a variety of approaches to help my clients achieve their goals depending on their individual needs.

My greatest strength as a Marriage and Family Therapist is helping my clients explore ways to make the changes in their lives that will allow them to live their life to their fullest potential. I help my clients achieve their personal life goals with a warm, safe, non-judgmental , and supportive environment. In doing so, my clients are encouraged to explore the issues that may be preventing them from living the life they desire. Thus, empowering them to take control of their personal journey to living a productive and meaningful life.

If you feel that you are ready to commit to bringing about positive changes in your life and would like support in exploring this path, I’m here to work with you in your journey to personal growth and development.

To schedule an appointment with Rosalindra Kowal, LMFT:

e-mail: rkjeb7@mailnest.example
Phone: (951)555-0147

Dena Holcroft

Dena Holcroft graduated with a Masters in Marriage and Family Therapy from Pellridge Crestwood College. She currently holds a license in Marriage and Family Therapy in the State of California. She is also formally trained in Clinical Art Therapy. Dena's expertise lies in providing treatment to individuals experiencing work-related injuries, severe physical and emotional pain, trauma, grief and loss, anxiety and depression. In her early career, she provided valuable service at the largest free clinic in the nation serving marginalized families and children. For the past ten years, Dena has worked with HIV/AIDS population.
Dena comes from a multicultural background and she has utilized this experience and knowledge in serving a variety of populations. At an organizational level, Dena has worked extensively with challenging issues such as the chemical dependency and homelessness. In her private practice, Dena is proficient in working within individuals experiencing relationship concerns, marital and family conflict, depression/anxiety, self-esteem concerns, adjustment disorders, and pain management. She has treated clients from diverse cultural, linguistic backgrounds and sexual orientations.
Dena is trained in Family Systems Theory and incorporates other strategies appropriate for each presenting issue. She specializes in Clinical Art Therapy and has successfully utilized an integrated approach including guided imagery and relaxation skills training for many years.

To schedule an appointment with Dena Holcroft, LMFT

e-mail: greypinestudio@inkmail.example
Phone: (951) 555-0169

Target Market(s)

Families with child development, marriage issues, or other mental health needs

Industry/Entity Type

Marketing

Number of Pages Required

5+ page

Requirements
Must have
• 1 home page, 1 about page, 1 contact page. About page could either be standalone page with 3 different bio pages for each therapist or an all in one about page that includes bios for all 3 therapists.

```html
<!DOCTYPE html>
<html lang="en">
<head>
<meta charset="utf-8">
<title>Meadowgate Counselors</title>
<link href="https://fonts.googleapis.com/css2?family=Open+Sans:wght@400;600;700&family=Raleway:wght@500;700&display=swap" rel="stylesheet">
<style>
:root{
  --green:#9bc53d;
  --green-dark:#7ea62c;
  --ink:#333;
  --muted:#777;
  --light:#eeeeee;
  --mint:#e6f2ee;
  --footer:#2e2e2e;
  --footer-bottom:#232323;
  --white:#fff;
}
*{margin:0;padding:0;box-sizing:border-box}
html,body{width:789px;height:1200px;overflow:hidden;background:var(--white)}
body{font-family:"Open Sans",Arial,sans-serif;color:var(--ink);position:relative}
.site-header{position:absolute;top:0;left:0;width:789px;height:92px;background:var(--white)}
.brand{position:absolute;left:88px;top:22px;display:flex;align-items:center;gap:10px}
.brand-mark{width:34px;height:34px;border-radius:50%;background:var(--green)}
.brand-name{font-family:"Raleway",sans-serif;font-weight:700;font-size:17px;color:var(--green-dark)}
.social{position:absolute;right:88px;top:0;display:flex;gap:4px}
.social span{width:22px;height:20px;background:var(--green)}
.contact-line{position:absolute;right:88px;top:38px;display:flex;gap:18px;font-size:10px;color:var(--ink);align-items:center}
.contact-line span{display:flex;align-items:center;gap:5px}
.phone-big{font-size:13px;font-weight:600}
.main-nav{position:absolute;right:88px;top:64px;font-size:10px;font-weight:600;display:flex;gap:10px;color:var(--ink)}
.main-nav i{color:#bbb;font-style:normal}
.hero{position:absolute;top:92px;left:0;width:789px;height:305px;
  background:radial-gradient(ellipse at 45% 55%,#ffd36a 0%,#f39a2b 30%,#b4541a 62%,#3a1d0e 100%)}
.hero-headline{position:absolute;left:190px;top:168px;width:410px;text-align:center;color:var(--white);
  font-family:"Raleway",sans-serif;font-weight:700;font-size:19px;line-height:25px;text-transform:uppercase;
  background:rgba(20,10,5,.35);padding:6px 10px}
.hero-arrow{position:absolute;top:185px}
.hero-dots{position:absolute;top:270px;left:367px;display:flex;gap:6px}
.hero-dots span{width:9px;height:9px;border-radius:50%;background:rgba(255,255,255,.6)}
.hero-dots span:first-child{background:var(--white)}
.hero-wave{position:absolute;left:0;top:370px}
.services{position:absolute;top:397px;left:0;width:789px;height:210px;background:var(--light)}
.service-card{position:absolute;top:14px;width:178px;height:180px;background:var(--white);text-align:center;padding:16px 12px}
.service-icon{width:52px;height:52px;border-radius:50%;background:var(--green);margin:0 auto 8px}
.service-card h3{font-size:10.5px;font-weight:700;line-height:13px;height:28px;margin-bottom:4px;display:flex;align-items:flex-end;justify-content:center}
.service-card p{font-size:8.5px;line-height:12px;color:var(--muted);height:36px}
.service-plus{width:14px;height:14px;background:var(--green);margin:10px auto 0;color:#fff;font-size:12px;line-height:14px;font-weight:700}
.welcome{position:absolute;top:612px;left:0;width:789px;height:218px;background:linear-gradient(90deg,#3b3b3b,#545454 60%,#3b3b3b)}
.welcome h2{position:absolute;left:88px;top:18px;width:322px;white-space:nowrap;font-family:"Raleway",sans-serif;font-weight:500;font-size:14px;line-height:18px;color:var(--white);text-transform:uppercase}
.welcome-rule{position:absolute;left:88px;top:42px;width:310px;height:2px;background:var(--green)}
.portrait{position:absolute;left:92px;top:56px;width:112px;height:112px;background:linear-gradient(160deg,#c9b6a6,#7a6b60);border:3px solid #fff}
.welcome-text{position:absolute;left:214px;top:54px;width:196px;font-size:8.5px;line-height:12.5px;color:#ddd}
.welcome-text.lower{left:92px;top:176px;width:318px}
.welcome-photo{position:absolute;left:420px;top:22px;width:236px;height:188px;background:linear-gradient(135deg,#a7c6a0,#e9d8c4 55%,#b79b84)}
.photo-arrows{position:absolute;left:612px;top:186px;display:flex;gap:3px}
.photo-arrows span{width:20px;height:18px;background:#555;display:flex;align-items:center;justify-content:center}
.testimonials{position:absolute;top:830px;left:0;width:789px;height:170px;background:var(--mint)}
.testimonials h2{position:absolute;top:16px;width:789px;text-align:center;font-family:"Raleway",sans-serif;font-weight:700;font-size:17px;color:var(--green-dark);text-transform:uppercase}
.quote{position:absolute;top:62px;display:flex;gap:10px;align-items:flex-start}
.avatar{width:52px;height:52px;border-radius:50%;background:linear-gradient(160deg,#b9a392,#5d4d44);flex:none;margin-top:8px}
.quote-box{background:var(--white);width:236px;padding:12px 12px;font-size:8.5px;line-height:12.5px;color:var(--muted);font-style:italic}
.quote-box b{display:block;font-style:normal;color:var(--green-dark);margin-top:4px;font-size:8.5px}
.site-footer{position:absolute;top:1000px;left:0;width:789px;height:172px;background:var(--footer);color:#ccc}
.footer-col{position:absolute;top:18px}
.footer-col h4{font-family:"Raleway",sans-serif;font-weight:500;font-size:14px;color:var(--green);text-transform:uppercase;margin-bottom:6px}
.footer-rule{width:150px;height:1px;background:#555;margin-bottom:10px}
.footer-col p,.footer-col li{font-size:8.5px;line-height:13px;list-style:none;display:flex;gap:6px;align-items:flex-start}
.footer-col li{margin-bottom:4px}
.field{width:166px;height:16px;background:#555;margin-bottom:6px;font-size:8px;color:#bbb;padding:2px 6px}
.field.tall{height:30px}
.btn{display:inline-block;background:var(--green);color:#fff;font-size:8px;font-weight:700;padding:3px 8px;text-transform:uppercase}
.footer-bottom{position:absolute;top:1172px;left:0;width:789px;height:28px;background:var(--footer-bottom);font-size:8.5px;color:#aaa}
.footer-links{position:absolute;left:88px;top:9px;display:flex;gap:8px}
.copyright{position:absolute;right:88px;top:9px}
</style>
</head>
<body>
<header class="site-header">
  <div class="brand"><span class="brand-mark"></span><span class="brand-name">Meadowgate Counselors</span></div>
  <div class="social" aria-label="Social links"><span></span><span></span><span></span><span></span></div>
  <div class="contact-line">
    <span><svg width="11" height="8" viewBox="0 0 11 8"><rect x="0.5" y="0.5" width="10" height="7" fill="none" stroke="#333"/><path d="M0.5 0.5 L5.5 4.5 L10.5 0.5" fill="none" stroke="#333"/></svg>marisel582@postbox.example</span>
    <span class="phone-big"><svg width="10" height="11" viewBox="0 0 10 11"><path d="M2 0h2l1 3-1.5 1a6 6 0 0 0 3 3L7.5 5.5l2.5 1v2.5c0 1-1 1.5-2 1.5C4 10 0 6 0 2c0-1 1-2 2-2z" fill="#333"/></svg>+123 456 7890</span>
  </div>
  <nav class="main-nav"><span>HOME</span><i>|</i><span>ABOUT US</span><i>|</i><span>CONTACT US</span></nav>
</header>

<section class="hero" role="img" aria-label="Family silhouettes playing at sunset">
  <svg class="hero-arrow" style="left:44px" width="12" height="22" viewBox="0 0 12 22"><path d="M10 2 L2 11 L10 20" fill="none" stroke="#fff" stroke-width="2"/></svg>
  <svg class="hero-arrow" style="right:44px" width="12" height="22" viewBox="0 0 12 22"><path d="M2 2 L10 11 L2 20" fill="none" stroke="#fff" stroke-width="2"/></svg>
  <h1 class="hero-headline">Lorem ipsum dolor sit amet consectetuer adipiscing elit sed diam nonummy nibh</h1>
  <div class="hero-dots"><span></span><span></span><span></span><span></span></div>
</section>
<svg class="hero-wave" width="789" height="32" viewBox="0 0 789 32"><path d="M0 22 Q394 -6 789 22 L789 32 L0 32 Z" fill="#eeeeee"/><path d="M0 22 Q394 -6 789 22" fill="none" stroke="#9bc53d" stroke-width="4"/></svg>

<section class="services">
  <article class="service-card" style="left:86px">
    <div class="service-icon"></div>
    <h3>Families With Child Developments</h3>
    <p>Gentle guidance helps parents and children grow together through every stage of early life.</p>
    <div class="service-plus">+</div>
  </article>
  <article class="service-card" style="left:306px">
    <div class="service-icon"></div>
    <h3>Marriage Issues</h3>
    <p>Couples learn to listen, rebuild trust and find calm ways through conflict at home.</p>
    <div class="service-plus">+</div>
  </article>
  <article class="service-card" style="left:525px">
    <div class="service-icon"></div>
    <h3>Mental Health Needs</h3>
    <p>Caring support for stress, anxiety, grief and low mood in a safe, private setting.</p>
    <div class="service-plus">+</div>
  </article>
</section>

<section class="welcome">
  <h2>Welcome to Meadowgate Counselors</h2>
  <div class="welcome-rule"></div>
  <div class="portrait" role="img" aria-label="Portrait of a therapist"></div>
  <p class="welcome-text">With over twenty years of combined clinical experience, our team works with adults, teens, children, families and couples. We focus on healthy relationships, easing depression and anxiety, and healing from trauma.</p>
  <p class="welcome-text lower">Feel free to explore each clinician and book an appointment with one of us today.</p>
  <div class="welcome-photo" role="img" aria-label="Parent and child holding hands"></div>
  <div class="photo-arrows">
    <span><svg width="6" height="10" viewBox="0 0 6 10"><path d="M5 1 L1 5 L5 9" fill="none" stroke="#fff" stroke-width="1.5"/></svg></span>
    <span><svg width="6" height="10" viewBox="0 0 6 10"><path d="M1 1 L5 5 L1 9" fill="none" stroke="#fff" stroke-width="1.5"/></svg></span>
  </div>
</section>

<section class="testimonials">
  <h2>What People Are Saying</h2>
  <div class="quote" style="left:88px">
    <div class="avatar" role="img" aria-label="Client photo"></div>
    <div class="quote-box">“I felt heard from the very first session. My family is closer and calmer than it has been in years.”<b>People Name</b></div>
  </div>
  <div class="quote" style="left:402px">
    <div class="avatar" role="img" aria-label="Client photo"></div>
    <div class="quote-box">“Kind, patient and practical advice. We learned real tools to talk through hard moments together.”<b>People Name</b></div>
  </div>
</section>

<footer class="site-footer">
  <div class="footer-col" style="left:88px">
    <h4>Contact Us</h4>
    <div class="footer-rule"></div>
    <ul>
      <li><svg width="8" height="10" viewBox="0 0 8 10"><path d="M4 0a4 4 0 0 1 4 4c0 3-4 6-4 6S0 7 0 4a4 4 0 0 1 4-4z" fill="#9bc53d"/></svg><span>Meadowgate Counselors<br>Riverside, California office</span></li>
      <li><svg width="8" height="9" viewBox="0 0 10 11"><path d="M2 0h2l1 3-1.5 1a6 6 0 0 0 3 3L7.5 5.5l2.5 1v2.5c0 1-1 1.5-2 1.5C4 10 0 6 0 2c0-1 1-2 2-2z" fill="#9bc53d"/></svg><span>(951)555-0182</span></li>
      <li><svg width="9" height="7" viewBox="0 0 11 8"><rect x="0.5" y="0.5" width="10" height="7" fill="none" stroke="#9bc53d"/><path d="M0.5 0.5 L5.5 4.5 L10.5 0.5" fill="none" stroke="#9bc53d"/></svg><span>marisel582@postbox.example</span></li>
    </ul>
  </div>
  <div class="footer-col" style="left:276px">
    <h4>Newsletter</h4>
    <div class="footer-rule"></div>
    <p style="width:170px;margin-bottom:8px">Sign up for news, tips and updates from our practice.</p>
    <div class="field">Your Name</div>
    <div class="field">Email Address</div>
    <span class="btn">Subscribe</span>
  </div>
  <div class="footer-col" style="left:487px">
    <h4>Quick Contact</h4>
    <div class="footer-rule"></div>
    <div class="field">Name</div>
    <div class="field">Email</div>
    <div class="field tall">Message</div>
    <span class="btn">Submit</span>
  </div>
</footer>
<div class="footer-bottom">
  <div class="footer-links"><span>Home</span><span>|</span><span>About Us</span><span>|</span><span>Contact Us</span></div>
  <div class="copyright">© Meadowgate Counselors 2015. All Rights Reserved</div>
</div>
</body>
</html>
```